Marlowe Gin (bottle label)

Marlowe Gin is a hand crafted spirit distilled by Tallbrook Distillery. The distillery is farm based. This is our first offering. The label is to be applied to a glass bottle.

We chose the name because we felt lucky to chance upon a great recipe. So we came up with Marlowe Gin. The phrase "Sometimes you get lucky" needs to be included. We'd like to see imagery of a lucky symbol such as a 4 leaf clover or shooting star. Elegant contrast come to mind. Reference to the distillery, bottle size (375ml) and Alc./vol. 40% is also needed. The distillery logo could be included. Or all is included in printed content.
Logo included for reference.
The label is rectangular.

Target Market(s)

Adults who enjoy fine spirits

Industry/Entity Type

Spirits distillation

Font styles to use
Serif
Script

Requirements
Must have
• classy, eye catching presentation
Nice to have
• Stylized 4 leaf clover or shooting star
Should not have
• Nothing hokey

```html
<!DOCTYPE html>
<html lang="en">
<head>
<meta charset="utf-8">
<title>Marlowe Gin – Label</title>
<link href="https://fonts.googleapis.com/css2?family=Courgette&family=Playfair+Display:wght@900&family=Tinos&display=swap" rel="stylesheet">
<style>
  :root {
    --backdrop: #8b8b8d;
    --paper: #f1f2f0;
    --ink: #2b2b2d;
    --gold: #c99a2e;
    --gold-light: #e2bf62;
  }
  * { margin: 0; padding: 0; box-sizing: border-box; }
  html, body { width: 1200px; height: 1200px; overflow: hidden; }
  body {
    background: var(--backdrop);
    display: flex; align-items: center; justify-content: center;
  }
  .label {
    position: relative;
    width: 600px; height: 1000px;
    color: var(--ink);
    text-align: center;
  }
  .label-frame { position: absolute; inset: 0; }
  .label-content { position: absolute; inset: 0; }
  .distillery {
    position: absolute; top: 80px; left: 0; right: 0;
    font-family: "Courgette", cursive;
    font-size: 38px; line-height: 1.15; color: var(--ink);
  }
  .distillery-mark {
    display: block; width: 14px; height: 14px; margin: 0 auto 10px;
    border-radius: 50%; background: var(--gold);
  }
  .product-name {
    position: absolute; top: 250px; left: 0; right: 0;
    font-family: "Courgette", cursive; font-size: 64px;
  }
  .gin-word {
    position: absolute; top: 360px; left: 0; right: 0;
    font-family: "Playfair Display", serif; font-weight: 900;
    font-size: 260px; line-height: 1; letter-spacing: 6px;
    color: var(--ink);
    text-shadow: 5px 3px 0 var(--gold);
  }
  .clover-art {
    position: absolute; top: 330px; left: 255px;
    width: 100px; height: 100px; border-radius: 50%;
    background: radial-gradient(circle, #d9d2b8 0%, #b9ad86 55%, rgba(241,242,240,0) 72%);
  }
  .shooting-star-art {
    position: absolute; top: 650px; left: 250px;
    width: 180px; height: 60px; border-radius: 30px;
    background: linear-gradient(100deg, rgba(43,43,45,0) 0%, rgba(43,43,45,0.25) 60%, rgba(43,43,45,0.6) 100%);
  }
  .tagline {
    position: absolute; top: 720px; left: 0; right: 0;
    font-family: "Courgette", cursive; font-size: 62px; line-height: 1.05;
  }
  .spec {
    position: absolute; bottom: 40px;
    font-family: "Tinos", serif; font-size: 26px; line-height: 1.2;
  }
  .spec-volume { left: 40px; }
  .spec-abv { right: 40px; text-align: right; }
</style>
</head>
<body>
  <div class="label">
    <svg class="label-frame" width="600" height="1000" viewBox="0 0 600 1000" aria-hidden="true">
      <path d="M50,4 H550 A46,46 0 0 0 596,50 V950 A46,46 0 0 0 550,996 H50 A46,46 0 0 0 4,950 V50 A46,46 0 0 0 50,4 Z"
            fill="var(--paper)" stroke="var(--gold)" stroke-width="8"/>
      <path d="M66,22 H534 A44,44 0 0 0 578,66 V934 A44,44 0 0 0 534,978 H66 A44,44 0 0 0 22,934 V66 A44,44 0 0 0 66,22 Z"
            fill="none" stroke="var(--gold-light)" stroke-width="3"/>
    </svg>
    <div class="label-content">
      <div class="distillery"><span class="distillery-mark"></span>Tallbrook<br>Distillery</div>
      <div class="product-name">Marlowe</div>
      <div class="gin-word">GIN</div>
      <div class="clover-art" role="img" aria-label="Engraved four leaf clover with radiating lines"></div>
      <div class="shooting-star-art" role="img" aria-label="Shooting star with trailing swoosh"></div>
      <div class="tagline">Sometimes you<br>get lucky</div>
      <div class="spec spec-volume">375ml</div>
      <div class="spec spec-abv">Alc./vol.<br>40%</div>
    </div>
  </div>
</body>
</html>
```